Business Card for Orvane Parts Wholesale supplier

Hi There! I need a new business card for our company. We are specialized in selling Orvane parts, mostly we sell new LCD screens for Telvox and Slatrons. I would like to see that back in the design.

You can find the colors and logo's on our website: www.dorvak-example.nl

Industry/Entity Type

Business

Contact Information for Business Card

My Details:
Lars Vintorp

Phone: 0031612873406
E-mail: Lars@dorvak-example.nl

Slogan: "Because Quality Matters"

Font styles to use
Sans Serif

Colors

Designer to choose colors to be used in the design.

Requirements
Must have
• A Black backside with the Dorvak logo on it. The front side should be clean with only my contact details.
• But I'm also open for something really different or awesome!
Nice to have
• Remember that we are in the parts & repairing industry, So i'll be handing those business cards mainly to repair companies. Maybe you can do something with that thought :)

```html
<!DOCTYPE html>
<html lang="en">
<head>
<meta charset="utf-8">
<title>Dorvak Business Card</title>
<link href="https://fonts.googleapis.com/css2?family=Open+Sans:wght@400;600;700&display=swap" rel="stylesheet">
<style>
  :root {
    --backdrop: #d9d9d7;
    --card: #1b1b1b;
    --card-edge: #111111;
    --brand-grey: #7a7a7a;
    --accent: #f08a1c;
    --text-light: #e6e6e6;
    --text-muted: #bdbdbd;
    --rule: #4a4a4a;
  }
  * { margin: 0; padding: 0; box-sizing: border-box; }
  html, body { width: 1200px; height: 647px; overflow: hidden; }
  body {
    background: var(--backdrop);
    font-family: "Open Sans", Arial, sans-serif;
    position: relative;
  }
  .card {
    position: absolute;
    top: 175px;
    width: 520px;
    height: 297px;
    background: linear-gradient(160deg, #222 0%, var(--card) 55%, var(--card-edge) 100%);
    border-bottom: 4px solid var(--accent);
    overflow: hidden;
  }
  .card--back { left: 50px; }
  .card--front { left: 630px; }

  /* Back side: brand name */
  .brand-large {
    position: absolute;
    left: 60px;
    top: 105px;
    display: flex;
    align-items: center;
    gap: 22px;
  }
  .brand-large__mark {
    width: 64px; height: 64px;
    background: var(--accent);
    border-radius: 50%;
  }
  .brand-large__name {
    font-size: 84px;
    font-weight: 700;
    color: var(--brand-grey);
    letter-spacing: 2px;
    line-height: 1;
  }

  /* Front side */
  .brand-small {
    position: absolute;
    left: 34px;
    top: 92px;
    display: flex;
    align-items: center;
    gap: 9px;
  }
  .brand-small__mark {
    width: 22px; height: 22px;
    background: var(--accent);
    border-radius: 50%;
  }
  .brand-small__name {
    font-size: 28px;
    font-weight: 700;
    color: var(--brand-grey);
    line-height: 1;
  }
  .holder {
    position: absolute;
    left: 34px;
    top: 140px;
    width: 170px;
    padding-bottom: 6px;
    border-bottom: 1px solid var(--rule);
    font-size: 15px;
    font-weight: 600;
    color: var(--accent);
  }
  .contacts {
    position: absolute;
    left: 34px;
    top: 196px;
    list-style: none;
    font-size: 11px;
    color: var(--text-muted);
  }
  .contacts li {
    display: flex;
    align-items: center;
    gap: 8px;
    margin-bottom: 6px;
  }
  .contacts svg { width: 10px; height: 10px; fill: var(--accent); flex: none; }
  .divider {
    position: absolute;
    left: 236px;
    top: 110px;
    width: 254px;
    height: 1px;
    background: var(--rule);
  }
  .slogan {
    position: absolute;
    right: 30px;
    top: 72px;
    font-size: 16px;
    color: var(--text-light);
  }
  .slogan em { font-style: normal; color: var(--accent); }
</style>
</head>
<body>

<section class="card card--back" aria-label="Card back">
  <div class="brand-large">
    <span class="brand-large__mark"></span>
    <span class="brand-large__name">dorvak</span>
  </div>
</section>

<section class="card card--front" aria-label="Card front">
  <div class="brand-small">
    <span class="brand-small__mark"></span>
    <span class="brand-small__name">dorvak</span>
  </div>
  <div class="divider"></div>
  <p class="slogan">Because <em>Quality</em> Matters</p>
  <p class="holder">Lars Vintorp</p>
  <ul class="contacts">
    <li>
      <svg viewBox="0 0 10 10" aria-hidden="true"><path d="M2 0.5 L3.8 2.6 L2.9 3.8 Q4 6 6.2 7.1 L7.4 6.2 L9.5 8 L8.3 9.6 Q4.5 9.5 2 6.5 Q0.3 4 0.4 1.7 Z"/></svg>
      0031612873406
    </li>
    <li>
      <svg viewBox="0 0 10 10" aria-hidden="true"><path d="M0 2 H10 V8.5 H0 Z M0.8 2.6 L5 5.6 L9.2 2.6" stroke="#1b1b1b" stroke-width="0.7"/></svg>
      Lars@dorvak-example.nl
    </li>
    <li>
      <svg viewBox="0 0 10 10" aria-hidden="true"><circle cx="5" cy="5" r="4.6"/><path d="M0.5 5 H9.5 M5 0.5 V9.5 M5 0.5 Q2 5 5 9.5 M5 0.5 Q8 5 5 9.5" stroke="#1b1b1b" stroke-width="0.6" fill="none"/></svg>
      www.dorvak-example.nl
    </li>
  </ul>
</section>

</body>
</html>
```